Visitenkarten-Design für Gesundheits- und Ernährungsberaterin
Zielgruppe
Ich bin Gesundheit und Ernährungsberaterin
Zielgruppe sind chronisch Kranke und Gesundheitsbewusste Personen
Aufgabenstellung
Schlichtes aber direkt erkennbares Design.
Mahl mit Maß , Gesundheit und Ernährungsberatung ( gut lesbar , elegant)
Marlene Obruk-Feistinger ( nicht so groß )
Grau ; Grün Töne und gerne etwas rosa
Infos wie Adresse und E-Mail vielleicht in jeweilige Blöcke am unteren Rand

```html
<!DOCTYPE html>
<html lang="de">
<head>
<meta charset="utf-8">
<title>Mahl mit Maß – Visitenkarten</title>
<link href="https://fonts.googleapis.com/css2?family=Cinzel:wght@400&display=swap" rel="stylesheet">
<style>
  :root {
    --green: #0a7d0a;
    --lime: #a9c93a;
    --orange: #ff6a00;
    --pink: #ff5fa2;
    --grey: #4b4b4b;
    --paper: #ffffff;
  }
  * { margin: 0; padding: 0; box-sizing: border-box; }
  html, body { width: 861px; height: 1200px; overflow: hidden; background: var(--paper); }
  body { position: relative; font-family: "Cinzel", serif; }

  .card {
    position: absolute;
    width: 336px; height: 220px;
    background: var(--paper);
    box-shadow: 3px 4px 8px rgba(0,0,0,0.28);
    overflow: hidden;
  }
  .card::before {
    content: ""; position: absolute; left: 0; top: 0; bottom: 0; width: 10px;
    background: var(--stripe);
  }
  .row-1 { top: 181px; } .row-2 { top: 476px; } .row-3 { top: 775px; }
  .col-front { left: 67px; } .col-back { left: 438px; }

  .theme-green  { --stripe: var(--green);  --mark: var(--pink);   --brand: var(--green); --tag: var(--green);  --info: var(--green); }
  .theme-lime   { --stripe: var(--lime);   --mark: var(--orange); --brand: var(--grey);  --tag: var(--orange); --info: var(--grey); }
  .theme-orange { --stripe: var(--orange); --mark: var(--orange); --brand: var(--grey);  --tag: var(--grey);   --info: var(--grey); }

  .brand-mark {
    position: absolute; display: flex; align-items: center; justify-content: center; gap: 8px;
    color: var(--brand); white-space: nowrap;
  }
  .brand-mark .dot { border-radius: 50%; background: var(--mark); flex: none; }
  .front .brand-mark { left: 10px; right: 0; top: 88px; font-size: 20px; }
  .front .brand-mark .dot { width: 22px; height: 22px; }
  .back .brand-mark { right: 10px; width: 150px; top: 42px; font-size: 14px; }
  .back .brand-mark .dot { width: 15px; height: 15px; }

  .tagline { position: absolute; text-align: center; color: var(--tag); line-height: 1.2; white-space: nowrap; }
  .front .tagline { left: 10px; right: 0; top: 154px; font-size: 10.5px; }
  .back .tagline { right: 8px; width: 154px; top: 91px; font-size: 8px; }

  .person { position: absolute; left: 22px; top: 131px; font-size: 11.5px; line-height: 1.25; color: var(--info); white-space: nowrap; }

  .address { position: absolute; left: 20px; top: 188px; font-size: 8.5px; line-height: 1.4; color: var(--info); white-space: nowrap; }
  .contact {
    position: absolute; left: 153px; top: 176px; font-size: 8.5px; line-height: 1.4; color: var(--info);
    display: grid; grid-template-columns: 41px auto; white-space: nowrap;
  }
</style>
</head>
<body>

  <section class="card front theme-green row-1 col-front">
    <div class="brand-mark"><span class="dot"></span><span>Mahl mit Maß</span></div>
    <p class="tagline">Mahl mit Maß , Gesundheits-<br>und Ernährungsberatung.</p>
  </section>
  <section class="card back theme-green row-1 col-back">
    <div class="brand-mark"><span class="dot"></span><span>Mahl mit Maß</span></div>
    <p class="tagline">Mahl mit Maß , Gesundheits-<br>und Ernährungsberatung.</p>
    <p class="person">Marlene<br>Obruk-Feistinger</p>
    <p class="address">Lindenweg 7<br>24999 Musterhude</p>
    <div class="contact"><span>Tel</span><span>04321 / 555 01 23</span><span>Mobil</span><span>0151 / 00 12 34 56</span><span>Mail</span><span>ernaehrung-mof@pmx.de</span></div>
  </section>

  <section class="card front theme-lime row-2 col-front">
    <div class="brand-mark"><span class="dot"></span><span>Mahl mit Maß</span></div>
    <p class="tagline">Mahl mit Maß , Gesundheits-<br>und Ernährungsberatung.</p>
  </section>
  <section class="card back theme-lime row-2 col-back">
    <div class="brand-mark"><span class="dot"></span><span>Mahl mit Maß</span></div>
    <p class="tagline">Mahl mit Maß , Gesundheits-<br>und Ernährungsberatung.</p>
    <p class="person">Marlene<br>Obruk-Feistinger</p>
    <p class="address">Lindenweg 7<br>24999 Musterhude</p>
    <div class="contact"><span>Tel</span><span>04321 / 555 01 23</span><span>Mobil</span><span>0151 / 00 12 34 56</span><span>Mail</span><span>ernaehrung-mof@pmx.de</span></div>
  </section>

  <section class="card front theme-orange row-3 col-front">
    <div class="brand-mark"><span class="dot"></span><span>Mahl mit Maß</span></div>
    <p class="tagline">Mahl mit Maß , Gesundheits-<br>und Ernährungsberatung.</p>
  </section>
  <section class="card back theme-orange row-3 col-back">
    <div class="brand-mark"><span class="dot"></span><span>Mahl mit Maß</span></div>
    <p class="tagline">Mahl mit Maß , Gesundheits-<br>und Ernährungsberatung.</p>
    <p class="person">Marlene<br>Obruk-Feistinger</p>
    <p class="address">Lindenweg 7<br>24999 Musterhude</p>
    <div class="contact"><span>Tel</span><span>04321 / 555 01 23</span><span>Mobil</span><span>0151 / 00 12 34 56</span><span>Mail</span><span>ernaehrung-mof@pmx.de</span></div>
  </section>

</body>
</html>
```